A new fitness program 10 WEEK FORGE needs to create a new mini-mag

We need the following word doc turned into a similar look and feel to our other programs (also attached). Images will be provided. It doesn't need to be over complex, but needs to keep the high quality and standards of our other booklets that focuses on male fitness and health.
The design includes creating the cover as well using a similar format to the example provided.

Fitness

```html
<!DOCTYPE html>
<html lang="en">
<head>
<meta charset="utf-8">
<title>10 Week Forge – 28 Day Primer Program Cover</title>
<link rel="stylesheet" href="https://fonts.googleapis.com/css2?family=Bitter:wght@800&family=Cinzel:wght@400;600&family=Courgette&family=Playfair+Display:wght@900&family=Open+Sans:wght@400;600&display=swap">
<style>
  :root {
    --page: #ffffff;
    --sky-top: #7fa8dc;
    --sky-mid: #a9c6ea;
    --sky-low: #c9d9ea;
    --sea: #6f9cb8;
    --skin: #c98f6c;
    --skin-light: #e0b393;
    --title-red: #8e1f1f;
    --ink: #1d2430;
    --white: #ffffff;
    --accent-yellow: #f1e26a;
    --shadow: rgba(0, 0, 0, 0.75);
  }
  * { margin: 0; padding: 0; box-sizing: border-box; }
  html, body {
    width: 1200px; height: 1147px; overflow: hidden;
    background: var(--page);
  }
  .cover {
    position: absolute; left: 225px; top: 44px;
    width: 750px; height: 1060px; overflow: hidden;
    background: linear-gradient(180deg, var(--sky-top) 0%, var(--sky-mid) 55%, var(--sky-low) 78%, var(--sea) 100%);
    box-shadow: 0 10px 30px rgba(0,0,0,0.18);
  }
  .cover__photo {
    position: absolute; left: 70px; top: 190px; width: 380px; height: 870px;
    background: radial-gradient(ellipse at 50% 40%, var(--skin-light) 0%, var(--skin) 55%, rgba(201,143,108,0) 80%);
  }
  .cover__title {
    position: absolute; left: 28px; top: 26px;
    font-family: "Bitter", serif; font-weight: 800; font-size: 44px;
    color: var(--title-red); letter-spacing: 0.5px;
    text-shadow: 2px 2px 0 var(--white), -1px -1px 0 var(--white);
  }
  .cover__subtitle {
    position: absolute; left: 30px; top: 88px;
    font-family: "Cinzel", serif; font-weight: 600; font-size: 23px; color: var(--ink);
  }
  .principles {
    position: absolute; left: 400px; top: 122px; list-style: none;
    font-family: "Cinzel", serif; font-size: 28px; color: var(--ink);
  }
  .principles li { display: flex; align-items: center; gap: 16px; height: 48px; }
  .principles svg { width: 30px; height: 30px; }
  .slogans {
    position: absolute; left: 380px; top: 300px; width: 350px;
    font-family: "Courgette", cursive; font-size: 27px; line-height: 44px; color: var(--white);
    text-shadow: 1px 1px 2px rgba(0,0,0,0.3);
  }
  .slogans .highlight { color: var(--accent-yellow); text-transform: uppercase; letter-spacing: 1px; }
  .slogans .line-2 { padding-left: 20px; }
  .slogans .line-3 { padding-left: 20px; }
  .motto {
    position: absolute; left: 430px; top: 560px; width: 300px;
    font-family: "Playfair Display", serif; font-weight: 900; font-size: 36px; line-height: 46px;
    color: var(--white); text-shadow: 3px 3px 4px var(--shadow);
  }
  .brand {
    position: absolute; right: 28px; top: 850px; text-align: right;
    font-family: "Open Sans", sans-serif; color: var(--white);
  }
  .brand__name { font-size: 24px; font-weight: 400; letter-spacing: 1px; }
  .brand__line { display: flex; align-items: center; justify-content: flex-end; gap: 10px; margin-top: 12px; }
  .brand__tagline { font-size: 22px; font-weight: 600; letter-spacing: 0.5px; }
  .brand__dot { width: 26px; height: 26px; border-radius: 50%; background: var(--white); }
  .brand__web { font-size: 21px; margin-top: 6px; }
</style>
</head>
<body>
  <main class="cover">
    <div class="cover__photo" role="img" aria-label="Photo of a shirtless athletic man in sunglasses and bright yellow board shorts standing on a beach under a blue sky"></div>

    <h1 class="cover__title">28 DAY “PRIMER” PROGRAM</h1>
    <p class="cover__subtitle">Enhance your life with the 3 core principles</p>

    <ul class="principles">
      <li><svg viewBox="0 0 30 30"><rect x="2" y="4" width="24" height="24" fill="none" stroke="#1d2430" stroke-width="2.5"/><path d="M6 15 L13 22 L28 3" fill="none" stroke="#1d2430" stroke-width="4"/></svg>MOTIVATION</li>
      <li><svg viewBox="0 0 30 30"><rect x="2" y="4" width="24" height="24" fill="none" stroke="#1d2430" stroke-width="2.5"/><path d="M6 15 L13 22 L28 3" fill="none" stroke="#1d2430" stroke-width="4"/></svg>EDUCATION</li>
      <li><svg viewBox="0 0 30 30"><rect x="2" y="4" width="24" height="24" fill="none" stroke="#1d2430" stroke-width="2.5"/><path d="M6 15 L13 22 L28 3" fill="none" stroke="#1d2430" stroke-width="4"/></svg>HABIT</li>
    </ul>

    <div class="slogans">
      <p class="line-1">Create a dominant <span class="highlight">mindset</span></p>
      <p class="line-2">Maximize your <span class="highlight">training</span></p>
      <p class="line-3">Understand the world of</p>
      <p class="line-4"><span class="highlight">nutrition</span></p>
    </div>

    <p class="motto">Life’s too short to be ‘AVERAGE’. It’s time to be the ‘BEST’!</p>

    <div class="brand">
      <p class="brand__name">10 WEEK FORGE</p>
      <div class="brand__line">
        <span class="brand__dot"></span>
        <span class="brand__tagline">MOTIVATION | EDUCATION | DOMINATION</span>
      </div>
      <p class="brand__web">www.10weekforge.com</p>
    </div>
  </main>
</body>
</html>
```